Upscale business cards needed for family office

We would like professional business cards created for employees of our family office. Relatively simple and straightforward, but also with a unique element to set them apart. Probably stick with neutral and simple colors that mesh well with the colors in the logo. We need space for the traditional elements, including name, title, address, email/phone number.

Industry/Entity Type

Business

Contact Information for Business Card

Space for name, title, phone number, email, address

```html
<!DOCTYPE html>
<html lang="en">
<head>
<meta charset="utf-8">
<title>M&amp;R Business Card</title>
<link rel="stylesheet" href="https://fonts.googleapis.com/css2?family=Rajdhani:wght@600&family=Roboto:wght@400&display=swap">
<style>
  :root {
    --bg: #e7e9eb;
    --card: #f3f3f2;
    --navy: #2d5590;
    --sky: #1796c4;
    --ink: #3c3c3c;
    --grey: #4a4a4a;
    --mark-frame: #9a9a9a;
  }
  html, body {
    margin: 0;
    padding: 0;
    width: 1200px;
    height: 1095px;
    overflow: hidden;
    background: var(--bg);
    font-family: "Roboto", Arial, sans-serif;
  }
  .canvas { position: relative; width: 1200px; height: 1095px; }
  .card {
    position: absolute;
    background: var(--card);
    box-shadow: 0 2px 4px rgba(0,0,0,0.12);
    overflow: hidden;
  }
  .card--front { left: 244px; top: 209px; width: 570px; height: 337px; }
  .card--front .accent-band {
    position: absolute; left: 0; right: 0; bottom: 0; height: 9px; background: var(--sky);
  }
  .card--back { left: 244px; top: 571px; width: 570px; height: 339px; }
  .card--back .side-band {
    position: absolute; left: 0; top: 0; bottom: 0; width: 49px; background: var(--navy);
  }
  .card--back .side-stripe {
    position: absolute; left: 49px; top: 0; bottom: 0; width: 6px; background: var(--sky);
  }
  .wordmark {
    position: absolute;
    display: flex;
    align-items: center;
    gap: 10px;
    color: var(--grey);
    font-family: "Roboto", Arial, sans-serif;
    font-weight: 400;
  }
  .wordmark__square { background: var(--sky); }
  .card--front .wordmark { left: 222px; top: 144px; font-size: 42px; }
  .card--front .wordmark__square { width: 22px; height: 22px; }
  .card--back .wordmark { left: 406px; top: 45px; font-size: 36px; }
  .card--back .wordmark__square { width: 18px; height: 18px; }
  .holder-name {
    position: absolute; left: 79px; top: 144px; margin: 0;
    font-family: "Rajdhani", "Arial Narrow", sans-serif;
    font-weight: 600; font-size: 24px; color: var(--ink);
  }
  .holder-title {
    position: absolute; left: 79px; top: 176px; margin: 0;
    font-size: 14px; color: var(--ink);
  }
  .contact-list {
    position: absolute; left: 79px; top: 223px; margin: 0; padding: 0; list-style: none;
    font-size: 16px; color: var(--ink);
  }
  .contact-list li { display: flex; align-items: center; height: 20.5px; }
  .contact-list svg { width: 13px; height: 13px; margin-right: 12px; fill: var(--ink); }
  .address {
    position: absolute; left: 79px; top: 294px; margin: 0;
    font-size: 16px; color: var(--ink);
  }
</style>
</head>
<body>
<div class="canvas">
  <section class="card card--front">
    <div class="wordmark"><span class="wordmark__square"></span><span>M&amp;R</span></div>
    <div class="accent-band"></div>
  </section>

  <section class="card card--back">
    <div class="side-band"></div>
    <div class="side-stripe"></div>
    <div class="wordmark"><span class="wordmark__square"></span><span>M&amp;R</span></div>
    <h1 class="holder-name">Your Good Name</h1>
    <p class="holder-title">Managing Director</p>
    <ul class="contact-list">
      <li>
        <svg viewBox="0 0 16 16" aria-hidden="true"><path d="M2 6c0-2 3-3 6-3s6 1 6 3v1h-3V5.5H5V7H2zM4 8h8l2 5H2z"/></svg>
        +00 111 222 3333
      </li>
      <li>
        <svg viewBox="0 0 16 16" aria-hidden="true"><path d="M1 3h14v10H1zM2.5 4.5 8 9l5.5-4.5z" fill-rule="evenodd"/></svg>
        yourname@yourwebsite.com
      </li>
      <li>
        <svg viewBox="0 0 16 16" aria-hidden="true"><path d="M8 1a7 7 0 1 0 0 14A7 7 0 0 0 8 1zm0 1.5c.8 0 1.8 1.8 2 4.5H6c.2-2.7 1.2-4.5 2-4.5zM2.6 7h2c.1-1.7.5-3.1 1-4A5.5 5.5 0 0 0 2.6 7zm8.8 0h2a5.5 5.5 0 0 0-3-4c.5.9.9 2.3 1 4zM2.6 9a5.5 5.5 0 0 0 3 4c-.5-.9-.9-2.3-1-4zm3.4 0c.2 2.7 1.2 4.5 2 4.5s1.8-1.8 2-4.5zm5.4 0c-.1 1.7-.5 3.1-1 4a5.5 5.5 0 0 0 3-4z"/></svg>
        www.yourwebsite.com
      </li>
    </ul>
    <p class="address">Your Long Commercial or business&nbsp; address in 2 line</p>
  </section>
</div>
</body>
</html>
```